Business Card Project for Firm Deck Hoisting

Business name is "Firm Deck Hoisting" we are a scaffolding & rigging business specialising in local and remote work for:
- scaffolding (residential, commercial, industrial)
- rigging
-man material hoists
- swing stages
- labour hire

On the back of the card I would like FDH as the symbol / logo. I have attached the logos we have had created by sketch harbour. We would like to use bold colours – preferably as the same colour scheme as the logo.

Target Market(s)

Construction business

Industry/Entity Type

Construction

Contact Information for Business Card

name: Owen Pellew
Title: Director
Phone: 0491 572 864
Address: PO BOX 3251, Paralowie SA 5108
Email: owen@firmdeckhoisting.com.au
Website: www.firmdeckhoisting.com.au

Font styles to use
Sans Serif

Requirements
Must have
• Must use existing logo & prefering using bold colours
Nice to have
• Would be nice to have a line of dot points in what we specialise in but not essential
• Would be nice to see some designs with a slogan but not essential
Should not have
• NA

```html
<!DOCTYPE html>
<html lang="en">
<head>
<meta charset="utf-8">
<title>Firm Deck Hoisting – Business Cards</title>
<link rel="stylesheet" href="https://fonts.googleapis.com/css2?family=Open+Sans:wght@400;600;700&display=swap">
<style>
  :root {
    --page-bg: #26292d;
    --card-white: #ffffff;
    --brand-blue: #1f6fc0;
    --brand-blue-light: #3d8bd2;
    --ink: #1c1d21;
    --ink-soft: #3a3c40;
  }
  * { box-sizing: border-box; margin: 0; padding: 0; }
  html, body {
    width: 1200px; height: 900px; overflow: hidden;
    background: var(--page-bg);
    font-family: "Open Sans", Arial, sans-serif;
  }
  .stage {
    position: relative; width: 1200px; height: 900px;
    display: flex; flex-direction: column; align-items: center; justify-content: center; gap: 56px;
  }
  .card {
    position: relative; width: 580px; height: 332px;
    background: var(--card-white);
    border-radius: 22px; overflow: hidden;
    box-shadow: 0 14px 30px rgba(0,0,0,.45);
  }
  .card-band {
    position: absolute; left: 0; right: 0; bottom: 0; height: 64px;
    background: linear-gradient(90deg, var(--brand-blue) 0%, var(--brand-blue-light) 100%);
  }
  .card-rule {
    position: absolute; left: 0; right: 0; bottom: 76px; height: 6px;
    background: var(--brand-blue);
  }
  .wordmark {
    display: flex; align-items: center; gap: 12px;
    font-weight: 700; color: var(--ink); letter-spacing: .02em;
    text-transform: uppercase; white-space: nowrap;
  }
  .wordmark-square { width: 16px; height: 16px; background: var(--brand-blue); flex: none; }
  .card--back .wordmark {
    position: absolute; left: 0; right: 0; top: 96px; justify-content: center; font-size: 30px;
  }
  .card--front .wordmark {
    position: absolute; right: 34px; top: 136px; font-size: 20px;
  }
  .card--front .wordmark-square { width: 12px; height: 12px; }
  .holder { position: absolute; left: 34px; top: 28px; }
  .holder-name { font-size: 24px; font-weight: 600; color: var(--ink); letter-spacing: .02em; text-transform: uppercase; }
  .holder-name span { color: var(--brand-blue); }
  .holder-title { font-size: 12px; font-weight: 700; color: var(--ink-soft); text-transform: uppercase; margin-top: 2px; }
  .holder-bar { width: 58px; height: 4px; background: var(--brand-blue); margin-top: 4px; }
  .contact-list { position: absolute; left: 34px; top: 118px; list-style: none; }
  .contact-list li {
    display: flex; align-items: center; gap: 10px;
    font-size: 13px; color: var(--ink-soft); height: 24px; white-space: nowrap;
  }
  .contact-list svg { width: 14px; height: 14px; flex: none; }
</style>
</head>
<body>
<main class="stage">
  <section class="card card--back" aria-label="Business card back">
    <div class="wordmark"><span class="wordmark-square"></span>Firm Deck Hoisting</div>
    <div class="card-rule"></div>
    <div class="card-band"></div>
  </section>

  <section class="card card--front" aria-label="Business card front">
    <div class="holder">
      <div class="holder-name">Owen <span>Pellew</span></div>
      <div class="holder-title">Director</div>
      <div class="holder-bar"></div>
    </div>
    <ul class="contact-list">
      <li>
        <svg viewBox="0 0 16 16" fill="none" stroke="#1f6fc0" stroke-width="1.4"><path d="M4 1.5l2.5 3-1.5 1.8c.8 1.8 2 3 3.8 3.8l1.7-1.5 3 2.5-1.3 2.4C6.8 13.5 2.5 9.2 1.5 3.8z"/></svg>
        0491 572 864
      </li>
      <li>
        <svg viewBox="0 0 16 16" fill="none" stroke="#1f6fc0" stroke-width="1.4"><rect x="1.5" y="3.5" width="13" height="9"/><path d="M1.5 3.5L8 9l6.5-5.5"/></svg>
        owen@firmdeckhoisting.com.au
      </li>
      <li>
        <svg viewBox="0 0 16 16" fill="none" stroke="#1f6fc0" stroke-width="1.3"><circle cx="8" cy="8" r="6.5"/><ellipse cx="8" cy="8" rx="3" ry="6.5"/><path d="M1.5 8h13M2.5 5h11M2.5 11h11"/></svg>
        www.firmdeckhoisting.com.au
      </li>
      <li>
        <svg viewBox="0 0 16 16" fill="none" stroke="#1f6fc0" stroke-width="1.4"><path d="M8 15s5-5 5-8.5a5 5 0 0 0-10 0C3 10 8 15 8 15z"/><circle cx="8" cy="6.5" r="1.8"/></svg>
        PO BOX 3251, Kestrel Vale SA 5190
      </li>
    </ul>
    <div class="wordmark"><span class="wordmark-square"></span>Firm Deck Hoisting</div>
    <div class="card-rule"></div>
    <div class="card-band"></div>
  </section>
</main>
</body>
</html>
```